Custom workshop/manufacture for custom furniture, architectural millwork and kitchen cabinetry

simple and clean. I like this website:
http://www.pebblelarchworks.com

Attached are random ideas

Target Market(s)

residential, commercial, hospitality, interior designers, architects, contractors

Coding

Coded - Design and coding required

Number of Pages Required

5+ page

Font styles to use
Other font styles liked:
• Avenir next

Requirements
Must have
• drop down menu for work - residential - commercial

```html
<!DOCTYPE html>
<html lang="en">
<head>
<meta charset="utf-8">
<title>Furniture co. — custom furniture</title>
<link rel="stylesheet" href="https://fonts.googleapis.com/css2?family=Montserrat:wght@400;600;700&family=Open+Sans:wght@300;400&family=Roboto:wght@400;500&display=swap">
<style>
  :root {
    --ink: #111111;
    --white: #ffffff;
    --muted: #b3b3b3;
    --hero-top: #6e6252;
    --hero-mid: #8a8170;
    --hero-low: #5a3a2a;
    --band-top: #86877f;
    --band-low: #6f7566;
  }
  * { margin: 0; padding: 0; box-sizing: border-box; }
  html, body { width: 1200px; height: 1200px; overflow: hidden; background: var(--white); }
  .page { position: relative; width: 1200px; height: 1200px; overflow: hidden; font-family: "Open Sans", sans-serif; color: var(--ink); }

  .site-header { position: absolute; top: 0; left: 0; width: 1200px; height: 62px; background: var(--white); z-index: 3; }
  .brand { position: absolute; left: 210px; top: 19px; display: flex; align-items: center; gap: 10px; font-family: "Roboto", sans-serif; font-size: 25px; font-weight: 400; color: var(--ink); }
  .brand-mark { width: 14px; height: 14px; border-radius: 50%; background: var(--ink); }
  .main-nav { position: absolute; top: 33px; left: 0; width: 1200px; font-family: "Roboto", sans-serif; font-size: 10px; font-weight: 500; letter-spacing: 0.2px; }
  .main-nav a { position: absolute; color: var(--ink); text-decoration: none; white-space: nowrap; }

  .hero-photo, .band-photo { position: absolute; left: 0; width: 1200px; }
  .hero-photo { top: 62px; height: 480px; }
  .band-photo { top: 800px; height: 360px; }

  .hero-copy { position: absolute; left: 218px; top: 172px; color: var(--white); z-index: 2; }
  .hero-title { font-family: "Montserrat", sans-serif; font-weight: 600; font-size: 88px; line-height: 64px; letter-spacing: -1px; }
  .hero-lead { margin-top: 26px; width: 530px; font-weight: 300; font-size: 14.5px; line-height: 19px; }
  .btn-more { display: inline-block; margin-top: 26px; width: 141px; height: 44px; border-radius: 22px; background: var(--ink); color: var(--white); font-family: "Montserrat", sans-serif; font-weight: 700; font-size: 11px; letter-spacing: -0.3px; line-height: 44px; text-align: center; text-decoration: none; }

  .features { position: absolute; top: 606px; left: 0; width: 1200px; }
  .feature { position: absolute; width: 260px; text-align: center; }
  .feature svg { display: block; margin: 0 auto; }
  .feature-title { margin-top: 15px; font-family: "Montserrat", sans-serif; font-weight: 400; font-size: 17px; }
  .feature-text { margin-top: 8px; font-weight: 300; font-size: 14px; line-height: 19px; color: var(--muted); }

  .tagline { position: absolute; top: 924px; left: 233px; width: 800px; text-align: center; color: var(--white); font-family: "Montserrat", sans-serif; font-weight: 600; font-size: 63px; line-height: 48px; letter-spacing: -0.5px; z-index: 2; }
</style>
</head>
<body>
<div class="page">
  <header class="site-header">
    <div class="brand"><span class="brand-mark"></span>Furniture co.</div>
    <nav class="main-nav">
      <a href="#" style="left:750px">HOME</a>
      <a href="#" style="left:812px">ABOUT US</a>
      <a href="#" style="left:893px">BLOG</a>
      <a href="#" style="left:950px">MEMBERSHIP</a>
      <a href="#" style="left:1048px">CONTACT US</a>
    </nav>
  </header>

  <svg class="hero-photo" viewBox="0 0 1200 480" role="img" aria-label="Living room with a brown armchair, footstool and potted plant">
    <defs>
      <linearGradient id="heroFill" x1="0" y1="0" x2="0" y2="1">
        <stop offset="0" stop-color="var(--hero-top)"/>
        <stop offset="0.6" stop-color="var(--hero-mid)"/>
        <stop offset="1" stop-color="var(--hero-low)"/>
      </linearGradient>
    </defs>
    <polygon points="0,0 1200,0 1200,367 0,479" fill="url(#heroFill)"/>
  </svg>

  <section class="hero-copy">
    <h1 class="hero-title">custom<br>furniture</h1>
    <p class="hero-lead">Custom workshop/manufacture for custom furniture, architectural millwork and kitchen cabinetry</p>
    <a class="btn-more" href="#">MORE ABOUT US</a>
  </section>

  <section class="features">
    <div class="feature" style="left:210px">
      <svg width="40" height="58" viewBox="0 0 40 58" fill="none" stroke="#111" stroke-width="2.2" stroke-linecap="round" stroke-linejoin="round">
        <path d="M20 3a16 16 0 0 0-9 29c2 2 3 4 3 7v4h12v-4c0-3 1-5 3-7A16 16 0 0 0 20 3z"/>
        <path d="M14 48h12M16 53h8M20 43V27M15 22l5 5 5-5"/>
      </svg>
      <h3 class="feature-title">creative designs</h3>
      <p class="feature-text">Short description regarding this feature of workshop / furnitures</p>
    </div>
    <div class="feature" style="left:503px">
      <svg width="40" height="58" viewBox="0 0 40 58" fill="none" stroke="#111" stroke-width="2.2" stroke-linejoin="round">
        <rect x="3" y="3" width="34" height="52" rx="4"/>
        <rect x="13" y="6" width="14" height="4" rx="1.5"/>
      </svg>
      <h3 class="feature-title">support services</h3>
      <p class="feature-text">Short description regarding this feature of workshop / furnitures</p>
    </div>
    <div class="feature" style="left:796px">
      <svg width="54" height="60" viewBox="0 0 54 60" fill="none" stroke="#111" stroke-width="2.2" stroke-linejoin="round">
        <path d="M7 18h40l5 39H2z"/>
        <path d="M17 22v-9a10 10 0 0 1 20 0v9"/>
        <circle cx="17" cy="23" r="1.2" fill="#111"/><circle cx="37" cy="23" r="1.2" fill="#111"/>
      </svg>
      <h3 class="feature-title">online ordering</h3>
      <p class="feature-text">Short description regarding this feature of workshop / furnitures</p>
    </div>
  </section>

  <svg class="band-photo" viewBox="0 0 1200 360" role="img" aria-label="White brick room with a wooden easel, green sofa and dried branches">
    <defs>
      <linearGradient id="bandFill" x1="0" y1="0" x2="0" y2="1">
        <stop offset="0" stop-color="var(--band-top)"/>
        <stop offset="1" stop-color="var(--band-low)"/>
      </linearGradient>
    </defs>
    <polygon points="0,120 1200,8 1200,246 0,358" fill="url(#bandFill)"/>
  </svg>

  <h2 class="tagline">we help your dream<br>design come true.</h2>
</div>
</body>
</html>
```